Cleaning Company needs a new business card design

Hi, We are looking for new business card designs to update with our latest logo and company information.
We would like to see designs using the colours:
Royal Blue #4169E1 - this is our company colour so this has to be in there. Please feel free to experiment with other colours.
Must include:
Front of business card:
Logo
Back of the business card:
0800 529 6081
07438 915 702
Email: info@pkrtidyhomes.co.uk
Web: www.pkrtidyhomes.co.uk
Services:
End of Tenancy
Carpet & Upholstery
Regular & One Off
all work fully insured.
The front of the business card with the logo can be made to look raised print. The blue man to be a shiny finish.
The business card needs to be presented in a matt finish
The business must be in the following styles:
Standard Square with rounded corners.
Thank you to all that take part in this.
Target Market(s)
Men and Women of different ages in the UK.
Industry/Entity Type
House Cleaning
Contact Information for Business Card
Front of business card:
Logo
0800 529 6081
07438 915 702
Email: pkrtidy@mailbox-demo.co.uk
Services:
End of Tenancy
Carpet & Upholstery
Regular & One Off
all work fully insured.

```html
<!DOCTYPE html>
<html lang="en">
<head>
<meta charset="utf-8">
<title>PKR Tidy Homes – Business Card</title>
<link href="https://fonts.googleapis.com/css2?family=Oswald:wght@300;400;500;600&display=swap" rel="stylesheet">
<style>
  :root {
    --royal: #0a52a6;
    --royal-light: #2f6fc0;
    --royal-deep: #0d3f80;
    --royal-pale: #5b8fd6;
    --icon-blue: #3f7fd4;
    --charcoal: #262626;
    --white: #ffffff;
    --mist: #d9dbe0;
    --text-light: #e6e6e6;
    --page: #ececec;
  }
  * { box-sizing: border-box; margin: 0; padding: 0; }
  html, body { width: 1200px; height: 1200px; overflow: hidden; }
  body {
    background: var(--page);
    font-family: "Oswald", sans-serif;
    display: flex;
    flex-direction: column;
    align-items: center;
    justify-content: center;
    gap: 48px;
  }
  .card {
    width: 800px;
    height: 516px;
    border-radius: 34px;
    overflow: hidden;
    position: relative;
    box-shadow: 0 6px 18px rgba(0,0,0,0.18);
  }

  /* Front */
  .card-front { background: var(--royal); }
  .front-band {
    position: absolute;
    left: 0; right: 0;
    top: 96px;
    height: 206px;
    background: var(--white);
    display: flex;
    align-items: center;
    justify-content: center;
  }
  .brand-name {
    font-weight: 500;
    font-size: 64px;
    color: var(--royal);
    letter-spacing: 1px;
    text-transform: uppercase;
    line-height: 1;
  }

  /* Back */
  .card-back { background: var(--charcoal); }
  .back-top {
    position: absolute;
    left: 0; right: 0; top: 0;
    height: 196px;
    background: linear-gradient(100deg, var(--royal-light) 0%, var(--royal) 45%, var(--royal-deep) 100%);
  }
  .back-bottom {
    position: absolute;
    left: 0; right: 0; bottom: 0;
    height: 42px;
    background: linear-gradient(90deg, var(--royal-light), var(--royal));
  }
  .headline {
    position: absolute;
    left: 60px;
    top: 70px;
    color: var(--white);
  }
  .headline-name {
    font-weight: 500;
    font-size: 46px;
    line-height: 1;
    text-transform: uppercase;
  }
  .headline-sub {
    font-weight: 300;
    font-size: 26px;
    color: var(--royal-pale);
    text-transform: uppercase;
    line-height: 1.1;
    padding-bottom: 6px;
    border-bottom: 1px solid rgba(255,255,255,0.45);
    width: 300px;
  }
  .headline-tag {
    font-weight: 600;
    font-size: 40px;
    text-transform: uppercase;
    line-height: 1.15;
    letter-spacing: 0.5px;
  }
  .back-brand {
    position: absolute;
    right: 60px;
    top: 86px;
    font-weight: 500;
    font-size: 44px;
    color: var(--mist);
    text-transform: uppercase;
    line-height: 1;
  }
  .contact-list {
    position: absolute;
    left: 60px;
    top: 262px;
    list-style: none;
    color: var(--text-light);
    font-weight: 300;
    font-size: 23px;
    text-transform: uppercase;
    line-height: 1;
  }
  .contact-list li {
    display: flex;
    align-items: center;
    gap: 12px;
    margin-bottom: 12px;
  }
  .contact-list svg { width: 22px; height: 22px; fill: var(--icon-blue); flex: none; }
  .services {
    position: absolute;
    right: 60px;
    top: 300px;
    color: var(--text-light);
    font-weight: 300;
    font-size: 25px;
    text-transform: uppercase;
    line-height: 1.25;
  }
  .services-title { font-weight: 400; }
</style>
</head>
<body>

  <section class="card card-front" aria-label="Business card front">
    <div class="front-band">
      <span class="brand-name">PKR Tidy Homes</span>
    </div>
  </section>

  <section class="card card-back" aria-label="Business card back">
    <div class="back-top"></div>
    <div class="back-bottom"></div>

    <div class="headline">
      <div class="headline-name">PKR</div>
      <div class="headline-sub">Tidy Homes</div>
      <div class="headline-tag">All work fully insured</div>
    </div>

    <div class="back-brand">PKR Tidy Homes</div>

    <ul class="contact-list">
      <li>
        <svg viewBox="0 0 24 24" aria-hidden="true"><path d="M6.6 10.8a15.1 15.1 0 0 0 6.6 6.6l2.2-2.2a1 1 0 0 1 1-.25 11.4 11.4 0 0 0 3.6.57 1 1 0 0 1 1 1V20a1 1 0 0 1-1 1A17 17 0 0 1 3 4a1 1 0 0 1 1-1h3.5a1 1 0 0 1 1 1c0 1.25.2 2.45.57 3.6a1 1 0 0 1-.25 1z"/></svg>
        0800 529 6081
      </li>
      <li>
        <svg viewBox="0 0 24 24" aria-hidden="true"><path d="M7 2h10a2 2 0 0 1 2 2v16a2 2 0 0 1-2 2H7a2 2 0 0 1-2-2V4a2 2 0 0 1 2-2zm0 3v12h10V5zm5 13.5a1 1 0 1 0 0 2 1 1 0 0 0 0-2z"/></svg>
        07438 915 702
      </li>
      <li>
        <svg viewBox="0 0 24 24" aria-hidden="true"><path d="M3 5h18a1 1 0 0 1 1 1v12a1 1 0 0 1-1 1H3a1 1 0 0 1-1-1V6a1 1 0 0 1 1-1zm1 2.2V17h16V7.2l-8 5.3z"/></svg>
        pkrtidy@mailbox-demo.co.uk
      </li>
      <li>
        <svg viewBox="0 0 24 24" aria-hidden="true"><path d="M12 2a10 10 0 1 0 0 20 10 10 0 0 0 0-20zm6.9 6h-3a15.6 15.6 0 0 0-1.4-3.6A8 8 0 0 1 18.9 8zM12 4c.8 1.2 1.5 2.5 1.9 4h-3.8c.4-1.5 1.1-2.8 1.9-4zM4.3 14a8 8 0 0 1 0-4h3.4a16.5 16.5 0 0 0 0 4zm.8 2h3a15.6 15.6 0 0 0 1.4 3.6A8 8 0 0 1 5.1 16zm3-8h-3a8 8 0 0 1 4.4-3.6A15.6 15.6 0 0 0 8.1 8zM12 20c-.8-1.2-1.5-2.5-1.9-4h3.8c-.4 1.5-1.1 2.8-1.9 4zm2.3-6H9.7a14.7 14.7 0 0 1 0-4h4.6a14.7 14.7 0 0 1 0 4zm.2 5.6a15.6 15.6 0 0 0 1.4-3.6h3a8 8 0 0 1-4.4 3.6zm1.8-5.6a16.5 16.5 0 0 0 0-4h3.4a8 8 0 0 1 0 4z"/></svg>
        www.pkrtidyhomes.co.uk
      </li>
    </ul>

    <div class="services">
      <div class="services-title">Services:</div>
      <div>-End of Tenancy</div>
      <div>-Carpet &amp; Upholstery</div>
      <div>-Regular &amp; One Off</div>
    </div>
  </section>

</body>
</html>
```